Corporate Word-document templates

We need these documents templates for the following types of documentation:

- Proposal
- Report (meetings)
- Solution description (technical)
- Documentation

The front page of the documents can take inspiration from our PowerPoint template, website (https://www.valdrenix.com/) and brand book. It should reflect our new branding guidelines.

See attached documents for structure and what we need them to contain. We need:
- front page
- generalt tekst page after the front page
- table of contents
- logo in upper right corner, page number + info in the footer, structure of tables
- anything else?

1) Make a design suggestion for the front page of the proposal and the Documentation
2) When we agree on the structure and front page, make the other two documents
3) we need all four documents with four different logos. 4 x 4 documents. the logos are: Quillmarsh, QMS, QMS Lumen & QMS Drift.

Target Market(s)

Large and medium corporations. Roles such as CEO, CFO, CIO, CTO, Controllers, Analysts, leaders/managers

Industry/Entity Type

Information Technology

Font styles to use
Sans Serif

Requirements
Must have
• - elements that are key to a word template
- four different word template files - each with the four different logos
- chose colors from our brand book

```html
<!DOCTYPE html>
<html lang="en">
<head>
<meta charset="utf-8">
<title>Quillmarsh – Document Templates</title>
<link href="https://fonts.googleapis.com/css2?family=Montserrat:wght@500;600;700;800&family=Arimo:wght@400;700&display=swap" rel="stylesheet">
<style>
  :root {
    --navy: #16325f;
    --navy-deep: #122a55;
    --teal: #1f7f98;
    --red: #e8514f;
    --red-soft: #f6d3d0;
    --ink: #2a2f3a;
    --muted: #6a7282;
    --paper: #ffffff;
    --stage-top: #a8a8a8;
    --stage-bottom: #9b9b9b;
  }
  * { box-sizing: border-box; margin: 0; padding: 0; }
  html, body { width: 1200px; height: 3557px; overflow: hidden; }
  body {
    position: relative;
    font-family: "Arimo", Arial, sans-serif;
    color: var(--ink);
    background: var(--stage-bottom);
  }
  .stage-top { position: absolute; left: 0; top: 0; width: 1200px; height: 1125px; background: var(--stage-top); }

  .page {
    position: absolute;
    width: 522px; height: 737px;
    background: var(--paper);
    box-shadow: 0 4px 14px rgba(0,0,0,.28);
    overflow: hidden;
  }
  .hero-cover { left: 327px; top: 177px; transform: scale(1.0805); transform-origin: top left; }
  .p-cover { left: 61px; top: 1194px; }
  .p-intro { left: 610px; top: 1194px; }
  .p-toc { left: 61px; top: 1961px; }
  .p-list { left: 610px; top: 1961px; }
  .p-table { left: 61px; top: 2725px; }
  .p-feature { left: 610px; top: 2725px; }

  /* cover */
  .cover { background: linear-gradient(180deg, #183a6c 0%, #1b4a7c 45%, #1f7d97 100%); color: #fff; }
  .cover-band { position: absolute; left: 0; top: 0; width: 100%; height: 117px; background: linear-gradient(180deg, #112755, #17356a); }
  .cover-logo { position: absolute; top: 34px; width: 100%; text-align: center; font-family: "Montserrat", sans-serif; font-weight: 700; font-size: 46px; letter-spacing: -.5px; color: #fff; }
  .cover-title { position: absolute; top: 146px; width: 100%; text-align: center; font-family: "Montserrat", sans-serif; font-weight: 800; line-height: 1; }
  .cover-title .l1 { display: block; color: var(--red); font-size: 41px; }
  .cover-title .l2 { display: block; color: #fff; font-size: 56px; margin-top: 6px; }
  .cover-rule { position: absolute; top: 267px; left: 203px; width: 117px; height: 4px; background: var(--red); }
  .cover-sub { position: absolute; top: 298px; width: 100%; text-align: center; font-family: "Montserrat", sans-serif; font-weight: 500; font-size: 17px; line-height: 22px; color: #fff; }
  .tablet { position: absolute; left: 119px; top: 370px; width: 420px; height: 380px; background: #0d0f14; border-radius: 30px 0 0 0; padding: 18px 0 0 26px; }
  .tablet-screen { width: 100%; height: 100%; background: linear-gradient(180deg, #2a2d35 0 22px, #f4f5f7 22px); }
  .cover-url { position: absolute; left: 0; top: 688px; width: 200px; height: 30px; background: #fff; border-radius: 0 15px 15px 0; display: flex; align-items: center; gap: 6px; padding-left: 16px; font-family: "Montserrat", sans-serif; font-weight: 700; font-size: 14px; letter-spacing: .6px; color: var(--navy); }

  /* running head and foot */
  .head-rule { position: absolute; top: 44px; left: 33px; width: 310px; height: 1.5px; background: var(--navy); }
  .head-logo { position: absolute; top: 34px; right: 37px; font-family: "Montserrat", sans-serif; font-weight: 700; font-size: 20px; letter-spacing: -.3px; color: var(--navy); }
  .foot-rule { position: absolute; top: 697px; left: 33px; width: 453px; height: 1.5px; background: var(--navy); z-index: 1; }
  .foot-url { position: absolute; top: 707px; left: 33px; display: flex; align-items: center; gap: 6px; font-size: 10.5px; letter-spacing: .6px; color: var(--navy); z-index: 1; }
  .foot-num { position: absolute; top: 700px; left: 465px; width: 21px; height: 22px; background: var(--navy); color: #fff; font-size: 11px; display: flex; align-items: center; justify-content: center; }

  /* intro page */
  .photo-col { position: absolute; left: 0; top: 0; width: 207px; height: 737px; background: linear-gradient(160deg, #8a6f59 0%, #5b4c42 35%, #3d4d63 70%, #2c3a4f 100%); }
  .photo-news { position: absolute; left: 217px; top: 253px; width: 305px; height: 230px; background: linear-gradient(120deg, #dfe2e6 0%, #b9bcc2 55%, #55585e 100%); }
  .intro-text { position: absolute; left: 220px; width: 268px; font-size: 12.2px; line-height: 16px; text-align: justify; color: #333; }
  .intro-text.t1 { top: 106px; }
  .intro-text.t2 { top: 512px; }
  .p-intro .head-rule { left: 217px; width: 126px; }
  .p-intro .foot-url { color: #fff; }

  /* headings */
  .h-title { position: absolute; left: 51px; top: 72px; font-family: "Montserrat", sans-serif; font-weight: 700; font-size: 22px; color: var(--navy); }
  .h-sub { position: absolute; left: 51px; top: 124px; font-family: "Montserrat", sans-serif; font-weight: 700; font-size: 14px; color: var(--navy); }
  .body-flow { position: absolute; left: 51px; top: 162px; width: 422px; font-size: 10.4px; line-height: 12.8px; color: #333; }
  .body-flow p { text-align: justify; }

  /* toc */
  .toc-title { position: absolute; left: 75px; top: 103px; font-family: "Montserrat", sans-serif; font-weight: 700; font-size: 21px; color: var(--navy); }
  .toc-title::after { content: ""; position: absolute; left: 0; top: 33px; width: 115px; height: 3px; background: var(--red); }
  .toc-list { position: absolute; left: 75px; top: 164px; width: 360px; list-style: none; }
  .toc-item { display: flex; align-items: center; height: 25.8px; font-size: 14px; color: #333; }
  .toc-item .label { width: 149px; }
  .toc-item.sub .label { padding-left: 12px; }
  .toc-item.main { font-weight: 700; color: var(--navy); }
  .toc-item.main.second { margin-top: 12px; }
  .toc-item .dots { width: 136px; border-bottom: 1px dashed #9aa0aa; height: 0; }
  .toc-item .num { margin-left: 49px; }

  /* label blocks */
  .tag { display: inline-block; background: var(--red); color: #fff; font-size: 10.5px; padding: 2px 14px; margin: 0 0 6px 0; }
  .block { margin-top: 16px; border-left: 2px solid var(--red); padding-left: 12px; }
  .block .tag { margin-left: -14px; }
  .bullets { list-style: none; margin-top: 5px; }
  .bullets li { position: relative; padding-left: 8px; margin-bottom: 3px; }
  .bullets li::before { content: "•"; position: absolute; left: 0; }

  /* table */
  .table-wrap { position: absolute; left: 52px; top: 287px; width: 416px; }
  .table-wrap .tag { margin: 0; }
  .table-wrap .tag-rule { height: 2px; background: var(--red); margin-bottom: 6px; }
  .data-table { border-collapse: separate; border-spacing: 3px 0; margin-left: -3px; width: calc(100% + 6px); font-size: 10.5px; }
  .data-table th, .data-table td { height: 26px; padding-left: 14px; text-align: left; font-weight: 400; }
  .data-table th { background: var(--red); color: #fff; }
  .data-table tr:nth-child(odd) td { background: var(--red-soft); }
  .data-table tr:nth-child(even) td { background: #fff; border-bottom: 1px solid var(--red-soft); }
  .table-after { position: absolute; left: 52px; top: 516px; width: 420px; font-size: 10.4px; line-height: 12.8px; text-align: justify; color: #333; }

  /* feature box */
  .feature-box { position: absolute; left: 52px; top: 359px; width: 415px; height: 283px; background: var(--red); display: flex; padding: 14px 6px; }
  .feature-col { flex: 1; display: flex; flex-direction: column; align-items: center; text-align: center; color: #fff; font-size: 10.4px; line-height: 12.6px; padding: 0 12px; }
  .feature-col + .feature-col { border-left: 1px dashed rgba(255,255,255,.8); }
  .feature-col svg { margin: 2px 0 10px; }
</style>
</head>
<body>

<div class="stage-top"></div>

<!-- hero cover -->
<section class="page cover hero-cover">
  <div class="cover-band"></div>
  <div class="cover-logo">Quillmarsh</div>
  <h1 class="cover-title"><span class="l1">UNLEASH BUSINESS</span><span class="l2">VALUE FASTER</span></h1>
  <div class="cover-rule"></div>
  <p class="cover-sub">User-friendly and effective solutions for planning,<br>analysis and execution – all gathered in one place.</p>
  <div class="tablet"><div class="tablet-screen" role="img" aria-label="Tablet showing a business dashboard with key figures and a bar chart"></div></div>
  <div class="cover-url">
    <svg width="14" height="14" viewBox="0 0 14 14" fill="none" stroke="currentColor" stroke-width="1.2"><circle cx="7" cy="7" r="6"/><ellipse cx="7" cy="7" rx="2.6" ry="6"/><path d="M1 7h12M2 4h10M2 10h10"/></svg>
    www.valdrenix.com
  </div>
</section>

<!-- cover -->
<section class="page cover p-cover">
  <div class="cover-band"></div>
  <div class="cover-logo">Quillmarsh</div>
  <h2 class="cover-title"><span class="l1">UNLEASH BUSINESS</span><span class="l2">VALUE FASTER</span></h2>
  <div class="cover-rule"></div>
  <p class="cover-sub">User-friendly and effective solutions for planning,<br>analysis and execution – all gathered in one place.</p>
  <div class="tablet"><div class="tablet-screen" role="img" aria-label="Tablet showing a business dashboard with key figures and a bar chart"></div></div>
  <div class="cover-url">
    <svg width="14" height="14" viewBox="0 0 14 14" fill="none" stroke="currentColor" stroke-width="1.2"><circle cx="7" cy="7" r="6"/><ellipse cx="7" cy="7" rx="2.6" ry="6"/><path d="M1 7h12M2 4h10M2 10h10"/></svg>
    www.valdrenix.com
  </div>
</section>

<!-- intro page -->
<section class="page p-intro">
  <div class="photo-col" role="img" aria-label="Photo of hands typing on a laptop next to a cup of tea"></div>
  <div class="head-rule"></div>
  <div class="head-logo">Quillmarsh</div>
  <p class="intro-text t1">Lorem Ipsum is simply dummy text of the printing and typesetting industry. Lorem Ipsum has been the industry's standard dummy text ever since the 1500s, when an unknown printer took a galley of type and scrambled it to make a type specimen book. It has survived not only five centuries.</p>
  <div class="photo-news" role="img" aria-label="Photo of a person reading a business newspaper"></div>
  <p class="intro-text t2">Lorem Ipsum is simply dummy text of the printing and typesetting industry. Lorem Ipsum has been the industry's standard dummy text ever since the 1500s, when an unknown printer took a galley of type and scrambled it to make a type specimen book. It has survived not only five centuries, but also the leap into electronic typesetting.</p>
  <div class="foot-rule"></div>
  <div class="foot-url"><svg width="13" height="13" viewBox="0 0 14 14" fill="none" stroke="currentColor" stroke-width="1.2"><circle cx="7" cy="7" r="6"/><ellipse cx="7" cy="7" rx="2.6" ry="6"/><path d="M1 7h12M2 4h10M2 10h10"/></svg>www.valdrenix.com</div>
  <div class="foot-num">2</div>
</section>

<!-- table of contents -->
<section class="page p-toc">
  <div class="head-rule"></div>
  <div class="head-logo">Quillmarsh</div>
  <h2 class="toc-title">TABLE OF CONTENT</h2>
  <ul class="toc-list">
    <li class="toc-item main"><span class="label">Heading Here</span><span class="dots"></span><span class="num">4</span></li>
    <li class="toc-item sub"><span class="label">Heading Here</span><span class="dots"></span><span class="num">5</span></li>
    <li class="toc-item sub"><span class="label">Heading Here</span><span class="dots"></span><span class="num">6</span></li>
    <li class="toc-item sub"><span class="label">Heading Here</span><span class="dots"></span><span class="num">7</span></li>
    <li class="toc-item sub"><span class="label">Heading Here</span><span class="dots"></span><span class="num">8</span></li>
    <li class="toc-item sub"><span class="label">Heading Here</span><span class="dots"></span><span class="num">9</span></li>
    <li class="toc-item sub"><span class="label">Heading Here</span><span class="dots"></span><span class="num">10</span></li>
    <li class="toc-item sub"><span class="label">Heading Here</span><span class="dots"></span><span class="num">11</span></li>
    <li class="toc-item main second"><span class="label">Heading Here</span><span class="dots"></span><span class="num">12</span></li>
    <li class="toc-item sub"><span class="label">Heading Here</span><span class="dots"></span><span class="num">13</span></li>
    <li class="toc-item sub"><span class="label">Heading Here</span><span class="dots"></span><span class="num">14</span></li>
    <li class="toc-item sub"><span class="label">Heading Here</span><span class="dots"></span><span class="num">15</span></li>
    <li class="toc-item sub"><span class="label">Heading Here</span><span class="dots"></span><span class="num">16</span></li>
    <li class="toc-item sub"><span class="label">Heading Here</span><span class="dots"></span><span class="num">17</span></li>
    <li class="toc-item sub"><span class="label">Heading Here</span><span class="dots"></span><span class="num">18</span></li>
    <li class="toc-item sub"><span class="label">Heading Here</span><span class="dots"></span><span class="num">19</span></li>
  </ul>
  <div class="foot-rule"></div>
  <div class="foot-url"><svg width="13" height="13" viewBox="0 0 14 14" fill="none" stroke="currentColor" stroke-width="1.2"><circle cx="7" cy="7" r="6"/><ellipse cx="7" cy="7" rx="2.6" ry="6"/><path d="M1 7h12M2 4h10M2 10h10"/></svg>www.valdrenix.com</div>
  <div class="foot-num">3</div>
</section>

<!-- list page -->
<section class="page p-list">
  <div class="head-rule"></div>
  <div class="head-logo">Quillmarsh</div>
  <h2 class="h-title">HEADING GOES HERE</h2>
  <h3 class="h-sub">Sub Heading Goes Here</h3>
  <div class="body-flow">
    <p>Lorem Ipsum is simply dummy text of the printing and typesetting industry. Lorem Ipsum has been the industry's standard dummy text ever.</p>
    <div class="block">
      <span class="tag">Text Goes Here</span>
      <ul class="bullets">
        <li>Lorem Ipsum is simply dummy text of the printing and typesetting.</li>
        <li>Lorem Ipsum is simply dummy text of the printing.</li>
        <li>Lorem Ipsum is simply dummy text of the printing and typesetting.</li>
      </ul>
    </div>
    <div class="block">
      <span class="tag">Text Goes Here</span>
      <p>Lorem Ipsum is simply dummy text of the printing and typesetting industry. Lorem Ipsum has been the industry's standard dummy text ever.</p>
    </div>
    <div class="block">
      <span class="tag">Text Goes Here</span>
      <p>Lorem Ipsum is simply dummy text of the printing and typesetting industry. Lorem Ipsum has been the industry's standard dummy text ever.</p>
      <ul class="bullets">
        <li>Lorem Ipsum is simply dummy text of the printing and typesetting.</li>
        <li>Lorem Ipsum is simply dummy text of the printing.</li>
        <li>Lorem Ipsum is simply dummy text of the printing and typesetting.</li>
        <li>Lorem Ipsum is simply dummy text of the printing.</li>
      </ul>
    </div>
    <div class="block">
      <span class="tag">Text Goes Here</span>
      <p>Lorem Ipsum is simply dummy text of the printing and typesetting industry. Lorem Ipsum has been the industry's standard dummy text ever since the 1500s, when an unknown printer took a galley of type and scrambled it to make a type specimen book. It has survived not only five centuries, but also the leap into electronic typesetting, remaining essentially unchanged.</p>
      <ul class="bullets">
        <li>Lorem Ipsum is simply dummy text of the printing and typesetting.</li>
        <li>Lorem Ipsum is simply dummy text of the printing.</li>
        <li>Lorem Ipsum is simply dummy text of the printing and typesetting.</li>
      </ul>
    </div>
  </div>
  <div class="foot-rule"></div>
  <div class="foot-url"><svg width="13" height="13" viewBox="0 0 14 14" fill="none" stroke="currentColor" stroke-width="1.2"><circle cx="7" cy="7" r="6"/><ellipse cx="7" cy="7" rx="2.6" ry="6"/><path d="M1 7h12M2 4h10M2 10h10"/></svg>www.valdrenix.com</div>
  <div class="foot-num">4</div>
</section>

<!-- table page -->
<section class="page p-table">
  <div class="head-rule"></div>
  <div class="head-logo">Quillmarsh</div>
  <h2 class="h-title">HEADING GOES HERE</h2>
  <h3 class="h-sub">Sub Heading Goes Here</h3>
  <div class="body-flow">
    <p>Lorem Ipsum is simply dummy text of the printing and typesetting industry. Lorem Ipsum has been the industry's standard dummy text ever since the 1500s, when an unknown printer took a galley of type and scrambled it to make a type specimen book. It has survived not only five centuries, but also the leap into electronic typesetting, remaining essentially unchanged. It was popularised in the 1960s with the release of Typeleaf sheets containing Lorem Ipsum passages, and more recently with desktop publishing software like Penwright Layout including versions of Lorem Ipsum.</p>
  </div>
  <div class="table-wrap">
    <span class="tag">Text Goes Here</span>
    <div class="tag-rule"></div>
    <table class="data-table">
      <thead><tr><th>Text Goes Here</th><th>Text Goes Here</th><th>Text Goes Here</th><th>Text Goes Here</th></tr></thead>
      <tbody>
        <tr><td>Text Goes Here</td><td>Text Goes Here</td><td>Text Goes Here</td><td>Text Goes Here</td></tr>
        <tr><td>Text Goes Here</td><td>Text Goes Here</td><td>Text Goes Here</td><td>Text Goes Here</td></tr>
        <tr><td>Text Goes Here</td><td>Text Goes Here</td><td>Text Goes Here</td><td>Text Goes Here</td></tr>
        <tr><td>Text Goes Here</td><td>Text Goes Here</td><td>Text Goes Here</td><td>Text Goes Here</td></tr>
        <tr><td>Text Goes Here</td><td>Text Goes Here</td><td>Text Goes Here</td><td>Text Goes Here</td></tr>
        <tr><td>Text Goes Here</td><td>Text Goes Here</td><td>Text Goes Here</td><td>Text Goes Here</td></tr>
      </tbody>
    </table>
  </div>
  <p class="table-after">Lorem Ipsum is simply dummy text of the printing and typesetting industry. Lorem Ipsum has been the industry's standard dummy text ever since the 1500s, when an unknown printer took a galley of type and scrambled it to make a type specimen book. It has survived not only five centuries, but also the leap into electronic typesetting, remaining essentially unchanged. It was popularised in the 1960s with the release of Typeleaf sheets containing Lorem Ipsum passages, and more recently with desktop publishing software like Penwright Layout including versions of Lorem Ipsum.</p>
  <div class="foot-rule"></div>
  <div class="foot-url"><svg width="13" height="13" viewBox="0 0 14 14" fill="none" stroke="currentColor" stroke-width="1.2"><circle cx="7" cy="7" r="6"/><ellipse cx="7" cy="7" rx="2.6" ry="6"/><path d="M1 7h12M2 4h10M2 10h10"/></svg>www.valdrenix.com</div>
  <div class="foot-num">5</div>
</section>

<!-- feature page -->
<section class="page p-feature">
  <div class="head-rule"></div>
  <div class="head-logo">Quillmarsh</div>
  <h2 class="h-title">HEADING GOES HERE</h2>
  <h3 class="h-sub">Sub Heading Goes Here</h3>
  <div class="body-flow">
    <p>Lorem Ipsum is simply dummy text of the printing and typesetting industry. Lorem Ipsum has been the industry's standard dummy text ever since the 1500s, when an unknown printer took a galley of type and scrambled it to make a type specimen book. It has survived not only five centuries, but also the leap into electronic typesetting, remaining essentially unchanged. It was popularised in the 1960s with the release of Typeleaf sheets containing Lorem Ipsum passages, and more recently with desktop publishing software like Penwright Layout including versions of Lorem Ipsum. Lorem Ipsum is simply dummy text of the printing and typesetting industry. Lorem Ipsum has been the industry's standard dummy text ever since the 1500s, when an unknown printer took a galley of type and scrambled it to make a type specimen book. It has survived not only five centuries, but also the leap into electronic typesetting, remaining essentially unchanged. It was popularised in the 1960s with the release of Typeleaf sheets containing Lorem Ipsum passages, and more recently with desktop publishing software like Penwright Layout including versions of Lorem Ipsum.</p>
  </div>
  <div class="feature-box">
    <div class="feature-col">
      <svg width="38" height="40" viewBox="0 0 38 40" fill="none" stroke="#fff" stroke-width="1.6"><path d="M4 2h20l10 10v26H4z"/><path d="M24 2v10h10"/><path d="M11 32v-6M17 32v-10M23 32v-13M29 32v-8"/></svg>
      <p>Lorem Ipsum is simply dummy text of the printing and typesetting industry. Lorem Ipsum has been the industry's standard dummy text ever since the 1500s, when an unknown printer took a galley of type and scrambled it to make a type specimen book. It has survived not only five centuries.</p>
    </div>
    <div class="feature-col">
      <svg width="38" height="40" viewBox="0 0 38 40" fill="none" stroke="#fff" stroke-width="1.6"><path d="M4 2h20l10 10v26H4z"/><path d="M24 2v10h10"/><path d="M11 32v-6M17 32v-10M23 32v-13M29 32v-8"/></svg>
      <p>Lorem Ipsum is simply dummy text of the printing and typesetting industry. Lorem Ipsum has been the industry's standard dummy text ever since the 1500s, when an unknown printer took a galley of type and scrambled it to make a type specimen book. It has survived not only five centuries.</p>
    </div>
    <div class="feature-col">
      <svg width="38" height="40" viewBox="0 0 38 40" fill="none" stroke="#fff" stroke-width="1.6"><path d="M4 2h20l10 10v26H4z"/><path d="M24 2v10h10"/><path d="M11 32v-6M17 32v-10M23 32v-13M29 32v-8"/></svg>
      <p>Lorem Ipsum is simply dummy text of the printing and typesetting industry. Lorem Ipsum has been the industry's standard dummy text ever since the 1500s, when an unknown printer took a galley of type and scrambled it to make a type specimen book. It has survived not only five centuries.</p>
    </div>
  </div>
  <div class="foot-rule"></div>
  <div class="foot-url"><svg width="13" height="13" viewBox="0 0 14 14" fill="none" stroke="currentColor" stroke-width="1.2"><circle cx="7" cy="7" r="6"/><ellipse cx="7" cy="7" rx="2.6" ry="6"/><path d="M1 7h12M2 4h10M2 10h10"/></svg>www.valdrenix.com</div>
  <div class="foot-num">6</div>
</section>

</body>
</html>
```